BELMORA needs a label for a Surface Cleaner with Alcohol

INTRODUCTION:
We are BELMORA, an experienced Spanish family-owned business specialized in manufacturing and distributing low-cost high-quality cleaning products in Spain, France and Portugal.

We are launching a new SURFACE CLEANER WITH ALCOHOL and we need an eye-catching label! We want to put your creativity to work! :D

CONCEPT:
Surface cleaner containing alcohol (not a disinfectant or hand sanitizer)

2 sizes

1) 750 ml PET cilinder white bottle with spray (bottle measures: 70mm diameter 230 mm height w/o spray)
Labels size (120mm base x 160mm height), 1 front label + 1 back label

2) 60 ml PET cilinder white bottle with spray (bottle 90mm height w/o spray x 35mm diameter) 1 label
Label size 110mm base x 60mm height

The design of the larger bottle must be adapted to the smaller bottle so as to make a collection

Label is in Spanish language (we are providing texts below)

GOAL:
To create a clean minimalist label with a “pharmaceutical” look and feel. Ideally by using colors and shapes to evoke a pharma green cross without explicitly using it. The pharma look and feel has to be visible from some distance. It must inspire safety and protection.

If you do mockups please use a 3D image of a bottle with sprayer (not the photo attached because it will look bad)

We love to see your ideas and be surprised with your proposals!

Thank you!

Target Market(s)

General public (non-professional) target, drugstore/supermaket, Spanish market mainly at the moment

Industry/Entity Type

Cleaning Product

Requirements
Must have
• Label front must have:
• - words: "LIMPIADOR HIGIENIZANTE" and "con ALCOHOL"
• - colors: white, pharma-looking light green, and a touch of blue
• - logo: BELMORA (brand), with the same pharma-looking green color
• - for the small bottle: a plane icon to point out that is suitable for travelling
• Label back side must contain this:
• - marketing text:
• “Limpiador higienizante para todo tipo de superfícies lavables. Su gran poder limpiador e higienizante elimina eficazmente la suciedad de zonas de contacto tales como asientos, inodoros, duchas, vidrios, pomos, manetas, asideros, barandillas, mesas, encimeras, suelos, mostradores, vitrinas, etc. No contiene lejía.”
• - icons:
• A column of 4-5 minimalist icons to clearly point out the applications (door knobs, seats, sink, handrail, toilet, floor, shower, glass,…) see icon examples attached for styling inspiration
• - legal text:
• “Líquido y vapores muy inflamables. Provoca irritación ocular grave. Puede provocar somnolencia o vértigo. Mantener alejado del calor, de superficies calientes, de chispas, de llamas abiertas y de cualquier otra fuente de ignición. No fumar. Mantener el recipiente herméticamente cerrado. Evitar respirar el polvo/el humo/el gas/la niebla/los vapores/el aerosol. Llevar guantes/prendas/gafas/máscara de protección. En caso de incendio emplear niebla de agua, espuma, productos químicos secos o dióxido de carbono ( CO2 ) para apagarlo. Almacenar en un lugar bien ventilado. Mantener el recipiente cerrado herméticamente. Mantener en lugar fresco.”
• - company identification:
• VESTA CORIN PRO SL
• B73925816
• C/ Valdemar 317 2-4
• 08147 Barcelona
• - pictograms: see the pictograms file
Nice to have
• Would be great to include:
• - seal: round seal with one or two words inside to give the feeling of “certified” or “approved”
• - a percetage number, like "100 % efectivo”
• - a small red “plus” sign referring for example to “+ higiene”
Should not have
• A plain green or red cross alone

```html
<!DOCTYPE html>
<html lang="es">
<head>
<meta charset="utf-8">
<title>BELMORA · Limpiador Higienizante con Alcohol</title>
<link href="https://fonts.googleapis.com/css2?family=Roboto+Condensed:wght@400;600;700&family=Roboto:wght@300&display=swap" rel="stylesheet">
<style>
  :root {
    --stage: #0b0b0b;
    --label-white: #ffffff;
    --pharma-green: #1f9e35;
    --pharma-green-light: #4cc95a;
    --pharma-green-dark: #0f8a24;
    --touch-blue: #5aa6f0;
  }
  * { margin: 0; padding: 0; box-sizing: border-box; }
  html, body {
    width: 1200px; height: 1100px; overflow: hidden;
    background: var(--stage);
  }
  .front-label {
    position: absolute; left: 332px; top: 50px;
    width: 536px; height: 1000px;
    background: var(--label-white);
    overflow: hidden;
  }
  .cross-blocks { position: absolute; inset: 0; }
  .label-text {
    position: absolute; left: 0; width: 100%;
    text-align: center;
  }
  .surface-tag {
    top: 138px;
    font-family: "Roboto", sans-serif; font-weight: 300;
    font-size: 44px; color: var(--pharma-green-light);
    letter-spacing: 1px;
  }
  .product-title {
    top: 385px;
    font-family: "Roboto Condensed", sans-serif; font-weight: 600;
    font-size: 72px; line-height: 76px; color: var(--pharma-green);
    letter-spacing: 3px;
  }
  .with-word {
    top: 782px;
    font-family: "Roboto Condensed", sans-serif; font-weight: 700;
    font-size: 34px; color: var(--pharma-green-dark);
  }
  .alcohol-word {
    top: 822px;
    font-family: "Roboto Condensed", sans-serif; font-weight: 400;
    font-size: 58px; color: var(--touch-blue);
    letter-spacing: 2px;
  }
  .brand-name {
    top: 895px;
    font-family: "Roboto Condensed", sans-serif; font-weight: 700;
    font-size: 52px; color: var(--pharma-green);
    letter-spacing: 2px;
  }
</style>
</head>
<body>
  <main class="front-label">
    <svg class="cross-blocks" width="536" height="1000" viewBox="0 0 536 1000" aria-hidden="true">
      <defs>
        <linearGradient id="block-left" x1="0" x2="1" y1="0" y2="0">
          <stop offset="0" stop-color="#0f8a24"/>
          <stop offset="0.55" stop-color="#1f9e35"/>
          <stop offset="1" stop-color="#5bd368"/>
        </linearGradient>
        <linearGradient id="block-right" x1="0" x2="1" y1="0" y2="0">
          <stop offset="0" stop-color="#5bd368"/>
          <stop offset="0.45" stop-color="#1f9e35"/>
          <stop offset="1" stop-color="#0f8a24"/>
        </linearGradient>
      </defs>
      <polygon points="18,0 128,0 128,340 0,340 0,150 18,150" fill="url(#block-left)"/>
      <polygon points="412,0 518,0 518,150 536,150 536,340 412,340" fill="url(#block-right)"/>
      <polygon points="0,620 128,620 128,1000 18,1000 18,830 0,830" fill="url(#block-left)"/>
      <polygon points="412,620 536,620 536,830 518,830 518,1000 412,1000" fill="url(#block-right)"/>
    </svg>

    <p class="label-text surface-tag">superficies</p>
    <h1 class="label-text product-title">LIMPIADOR<br>HIGIENIZANTE</h1>
    <p class="label-text with-word">con</p>
    <p class="label-text alcohol-word">ALCOHOL</p>
    <p class="label-text brand-name">BELMORA</p>
  </main>
</body>
</html>
```